Training company needs a Quick Reference Card design

We have draft skeleton of the design and most of the text. But we need a designer to take it the rest if the way.
I have designed a 2 page quick reference card - it is meant to be a 2-sided document. The first page is portrait, the back page can either be portrait or landscape, I'm not too concerned, whichever fits best.
Section called 'Maps' on front, a map is a collection of documents (like a manual), a topic is a document (like a page or section of a manual) and a block is a section of a document. The graphic is mean to illustrate the hierarchy but essentially a map is a big document with smaller documents in it.
Please use the company's logo colors to differentiate the different sections with minimal/ highlight only use of the darkest color, preferably.
Please use the icons for the corresponding Information types in the chart of the back - except please re-design the icons color scheme to match the company's logo/website colors.

Target Market(s)

Technical writers, after attending our training course, as an ongoing resource for them

Industry/Entity Type

It Company

Font styles to use
Sans Serif

Requirements
Must have
• Must adhere to look and feel of brand/ website. www.lumenrivet.com
Nice to have
• Please keep the design modern and slick looking, not too busy, easy to read

```html
<!DOCTYPE html>
<html lang="en">
<head>
<meta charset="utf-8">
<title>Quick Reference Card – Lumen Rivet</title>
<link href="https://fonts.googleapis.com/css2?family=Exo+2:wght@500;600;700&family=Nunito+Sans:wght@400;600;700&display=swap" rel="stylesheet">
<style>
  :root {
    --navy: #1c1a8e;
    --cyan: #00a3d9;
    --ink: #111111;
    --frame: #000000;
    --paper: #ffffff;
    --card-edge: #c9c9d6;
    --heading: "Exo 2", "Arial", sans-serif;
    --body: "Nunito Sans", "Arial", sans-serif;
  }
  * { box-sizing: border-box; margin: 0; padding: 0; }
  html, body { width: 892px; height: 1200px; overflow: hidden; background: var(--frame); }
  .sheet {
    position: relative;
    width: 892px; height: 1200px;
    border: 14px solid var(--frame);
    background: var(--paper);
    font-family: var(--body);
    color: var(--ink);
  }
  .section {
    position: absolute;
    background: var(--navy);
    border-radius: 6px;
  }
  .panel {
    background: var(--paper);
    border: 2px solid var(--card-edge);
    border-radius: 8px;
    position: absolute;
  }

  /* Header */
  .masthead { position: absolute; left: 12px; top: 8px; width: 852px; height: 92px; display: flex; align-items: center; }
  .brand { display: flex; align-items: center; gap: 12px; width: 262px; }
  .brand-dot { width: 62px; height: 62px; border-radius: 50%; background: var(--navy); flex: none; }
  .brand-name { font-family: var(--heading); font-weight: 700; font-size: 25px; line-height: 1.05; color: var(--navy); }
  .masthead-rule { width: 2px; height: 62px; background: var(--navy); margin: 0 18px 0 8px; }
  .doc-title { font-family: var(--heading); font-weight: 700; font-size: 40px; letter-spacing: 1.5px; color: var(--navy); white-space: nowrap; }
  .doc-title span { color: var(--cyan); }
  .header-rule { position: absolute; left: 14px; top: 104px; width: 836px; height: 6px; border-top: 2px solid var(--cyan); border-bottom: 2px solid var(--navy); }

  .section-title { font-family: var(--heading); font-weight: 700; color: var(--paper); text-align: center; font-size: 27px; letter-spacing: 1px; }

  /* Map */
  .map { left: 0; top: 120px; width: 402px; height: 281px; }
  .map .section-title { margin-top: 8px; }
  .topic { top: 50px; width: 191px; height: 222px; padding: 8px; text-align: center; }
  .topic:nth-of-type(1) { left: 9px; }
  .topic:nth-of-type(2) { left: 202px; }
  .topic h3 { font-family: var(--heading); font-weight: 600; color: var(--navy); font-size: 23px; margin: 2px 0 8px; }
  .block {
    background: var(--cyan); color: var(--paper);
    font-family: var(--heading); font-weight: 700; font-size: 18px; line-height: 1.1;
    height: 77px; display: flex; align-items: center; justify-content: center;
  }
  .block + .block { margin-top: 10px; }

  .glossary { left: 409px; top: 120px; width: 441px; height: 281px; padding: 10px 9px; display: flex; flex-direction: column; gap: 10px; }
  .term { position: static; flex: 1; display: flex; align-items: center; justify-content: center; text-align: center; font-size: 15.5px; line-height: 1.3; padding: 4px 14px; }
  .term b { color: var(--cyan); font-weight: 700; }

  /* Writing rules */
  .rules { left: 0; top: 409px; width: 850px; height: 261px; }
  .rules .section-title { margin-top: 8px; }
  .rule { top: 49px; width: 276px; height: 204px; padding: 10px 12px; text-align: center; }
  .rule:nth-of-type(1) { left: 6px; }
  .rule:nth-of-type(2) { left: 288px; }
  .rule:nth-of-type(3) { left: 571px; width: 274px; }
  .rule h3 { font-family: var(--heading); font-weight: 600; color: var(--navy); font-size: 25px; line-height: 1.08; letter-spacing: 1px; margin-bottom: 14px; }
  .rule p { font-size: 15.5px; line-height: 1.4; }

  /* Questions + language arts */
  .questions { left: 0; top: 678px; width: 483px; height: 214px; }
  .questions .panel { left: 6px; top: 8px; width: 471px; height: 198px; padding: 14px 18px; }
  .questions h3 { font-family: var(--heading); font-weight: 600; color: var(--navy); font-size: 22px; line-height: 1.12; text-align: center; margin-bottom: 12px; }
  .questions ol { list-style: none; font-size: 18px; line-height: 1.25; }
  .questions li { display: flex; gap: 14px; margin-bottom: 8px; }
  .questions li span { flex: none; width: 22px; }

  .arts { left: 490px; top: 678px; width: 360px; height: 214px; }
  .arts .panel { left: 6px; top: 8px; width: 348px; height: 198px; padding: 10px 12px; text-align: center; }
  .arts h3 { font-family: var(--heading); font-weight: 600; color: var(--navy); font-size: 22px; line-height: 1.1; }
  .arts .acronym { font-family: var(--heading); font-weight: 600; color: var(--cyan); font-size: 24px; line-height: 1.1; margin-top: 2px; }
  .arts p { font-size: 18px; line-height: 1.15; }

  /* Cognitive principles */
  .principles { left: 0; top: 900px; width: 850px; height: 272px; }
  .principles .section-title { margin-top: 6px; }
  .principle { top: 48px; width: 205px; height: 216px; padding: 10px 10px; text-align: center; }
  .principle:nth-of-type(1) { left: 6px; }
  .principle:nth-of-type(2) { left: 218px; }
  .principle:nth-of-type(3) { left: 430px; }
  .principle:nth-of-type(4) { left: 642px; }
  .principle h3 { font-family: var(--heading); font-weight: 600; color: var(--navy); font-size: 22px; letter-spacing: 0.5px; margin-bottom: 10px; }
  .principle p { font-size: 15.5px; line-height: 1.4; }
</style>
</head>
<body>
<main class="sheet">
  <header>
    <div class="masthead">
      <div class="brand">
        <div class="brand-dot"></div>
        <div class="brand-name">LUMENRIVET<br>.com</div>
      </div>
      <div class="masthead-rule"></div>
      <h1 class="doc-title">QUICK REFERENCE <span>CARD</span></h1>
    </div>
    <div class="header-rule"></div>
  </header>

  <section class="section map">
    <h2 class="section-title">MAP</h2>
    <div class="panel topic">
      <h3>TOPIC</h3>
      <div class="block">PRIMARY<br>BLOCK</div>
      <div class="block">SUB-BLOCK</div>
    </div>
    <div class="panel topic">
      <h3>TOPIC</h3>
      <div class="block">PRIMARY<br>BLOCK</div>
      <div class="block">SUB-BLOCK</div>
    </div>
  </section>

  <section class="section glossary">
    <p class="panel term"><span><b>A map</b> is a file that organizes topics into structured collections of information. Maps specify hierarchy and relationships among topics.</span></p>
    <p class="panel term"><span><b>A topic</b> is a group of related blocks with a title. Use the chunking principle to group together relevant blocks.</span></p>
    <p class="panel term"><span><b>A block</b> is a bite-sized chunk of information about one main idea that allows the writer to organize the material into logical sections.</span></p>
  </section>

  <section class="section rules">
    <h2 class="section-title">GENERAL WRITING RULES</h2>
    <div class="panel rule">
      <h3>EFFECTIVE<br>SENTENCES</h3>
      <p>One main agent, action &amp; outcome. Use active voice and simplest tense possible. No more than 7 sentences per paragraph. Use lists and tables.</p>
    </div>
    <div class="panel rule">
      <h3>SPECIAL<br>CHARACTERS</h3>
      <p>Avoid special characters, spell out words instead. Remove parentheses, colons and dashes. Avoid using quotation marks and slashes.</p>
    </div>
    <div class="panel rule">
      <h3>PLAIN<br>LANGUAGE</h3>
      <p>Write in short sentences. Provide useful titles. Use clear familiar words. Avoid excess words. Be consistent.</p>
    </div>
  </section>

  <section class="section questions">
    <div class="panel">
      <h3>3 QUESTIONS TO ASK BEFORE<br>YOU START WRITING</h3>
      <ol>
        <li><span>1.</span>What is the purpose of this information?</li>
        <li><span>2.</span>What is the desired user response of this information?</li>
        <li><span>3.</span>Who is the audience?</li>
      </ol>
    </div>
  </section>

  <section class="section arts">
    <div class="panel">
      <h3>2 TYPES OF<br>LANGUAGE ARTS:</h3>
      <div class="acronym">LAFI</div>
      <p>Language arts for information</p>
      <div class="acronym">LAFPR</div>
      <p>language arts for personal response</p>
    </div>
  </section>

  <section class="section principles">
    <h2 class="section-title">4 COGNITIVE PRINCIPLES</h2>
    <div class="panel principle">
      <h3>CONSISTENCY</h3>
      <p>Use similar terms and structures. Pick a term and stick with it. Use the same sequence of blocks. Use consistent styles.</p>
    </div>
    <div class="panel principle">
      <h3>CHUNKING</h3>
      <p>Maximum of nine (7 +/- 2) items in a list, rows in a table, blocks in a topic, or topics in a map.</p>
    </div>
    <div class="panel principle">
      <h3>RELEVANCE</h3>
      <p>Group similar items together. Separate relevance? Separate block. Irrelevant? Delete it.</p>
    </div>
    <div class="panel principle">
      <h3>TITLING</h3>
      <p>Name everything. Name every block, every topic, every map and every table column.</p>
    </div>
  </section>
</main>
</body>
</html>
```